Business Card & Email Signature Design || Upmarket + Luxury

Riverlume Honey, a New Zealand Manuka Honey company needs a Business Card & Email Signature design.

Our logo's are attached in Gold & Black versions, feel free to be creative with how you use the logo and it's patterns in your design.

Style:
- Looking for an Elegant, Luxurious, Upmarket feel.
- Black/Matte Black Card, Gold Foil, UV Embossing

Information to Add:

- Logo
- Company Name: Riverlume Honey
- Name: Mattias Brovell
- Title: Creative Director
- Phone: +64 2919 58 617
- Email: mattias@riverlumehoney.example
- Website: www.riverlumehoney.example

- Socials: ***For email Signature Only***
- Facebook: https://social-one.example/riverlumehoney
- Instagram: https://social-two.example/riverlumehoney

Target Market(s)

Asia/Europe Luxury, Upmarket

Contact Information for Business Card

- Logo
- Name: Mattias Brovell
- Phone: +64 2919 58 617

Font styles to use
Other font styles liked:
• Champagne & Limousines (Attached)

Requirements
Must have
• Business Card & Email Signature Design.

Looking for a Sleek, Luxury, Upmarket Design.

```html
<!DOCTYPE html>
<html lang="en">
<head>
<meta charset="utf-8">
<title>Riverlume Honey – Business Card &amp; Email Signature</title>
<link rel="stylesheet" href="https://fonts.googleapis.com/css2?family=Jost:wght@300;400;500&display=swap">
<style>
  :root {
    --stage-top: #d9d9db;
    --stage-bottom: #e6e6e8;
    --paper: #ffffff;
    --card-black: #0b0708;
    --foil-gold: #d6b96f;
    --foil-deep: #a8863c;
    --ink: #231f20;
    --badge-ring: #6b6460;
  }
  * { margin: 0; padding: 0; box-sizing: border-box; }
  html, body { width: 1200px; height: 916px; overflow: hidden; }
  body {
    position: relative;
    background: var(--paper);
    font-family: "Jost", "Futura", sans-serif;
    font-weight: 300;
  }
  .card-stage {
    position: absolute; left: 0; top: 0; width: 1200px; height: 572px;
    background: linear-gradient(180deg, var(--stage-top), var(--stage-bottom));
  }
  .card {
    position: absolute; top: 152px; width: 406px; height: 245px;
    background: var(--card-black);
    color: var(--foil-gold);
  }
  .card--front { left: 134px; }
  .card--back { left: 636px; text-align: center; }

  .front-badge { position: absolute; left: 53px; top: 47px; }
  .front-badge__name {
    position: absolute; left: 53px; top: 110px; width: 152px;
    text-align: center; font-size: 15px; font-weight: 400;
    letter-spacing: 2px; text-transform: uppercase; line-height: 1.25;
    color: var(--foil-gold);
  }
  .front-ornament {
    position: absolute; left: 236px; top: 70px; width: 96px; height: 108px;
    border-radius: 50% 50% 48% 48%;
    background: radial-gradient(circle at 50% 50%, var(--foil-gold), var(--foil-deep) 70%, var(--card-black) 100%);
    opacity: .85;
  }

  .back-mark { position: absolute; left: 191px; top: 18px; }
  .back-brand {
    position: absolute; left: 0; top: 66px; width: 100%;
    font-size: 15px; font-weight: 400; letter-spacing: 3px; text-transform: uppercase;
  }
  .back-name {
    position: absolute; left: 0; top: 101px; width: 100%;
    font-size: 26px; font-weight: 400; letter-spacing: 4px; text-transform: uppercase;
    line-height: 34px;
  }
  .back-title {
    position: absolute; left: 0; top: 133px; width: 100%;
    font-size: 12px; font-weight: 500; letter-spacing: 2.5px; text-transform: uppercase;
  }
  .back-phone { position: absolute; left: 0; top: 153px; width: 100%; font-size: 17px; letter-spacing: 1px; }
  .back-email { position: absolute; left: 0; top: 176px; width: 100%; font-size: 14px; letter-spacing: .8px; }
  .back-web { position: absolute; left: 0; top: 211px; width: 100%; font-size: 13px; letter-spacing: .8px; }

  .signature-badge { position: absolute; left: 186px; top: 663px; }
  .signature-badge__name {
    position: absolute; left: 196px; top: 727px; width: 142px;
    text-align: center; font-size: 15px; font-weight: 400; letter-spacing: 2px;
    text-transform: uppercase; line-height: 1.25; color: var(--ink);
  }
  .signature { position: absolute; left: 516px; top: 644px; color: var(--ink); }
  .signature__name { font-size: 35px; font-weight: 400; letter-spacing: 7px; text-transform: uppercase; line-height: 40px; }
  .signature__title { font-size: 17px; font-weight: 400; letter-spacing: 3.5px; text-transform: uppercase; line-height: 20px; }
  .signature__contacts { margin-top: 22px; font-size: 24px; line-height: 29px; letter-spacing: .6px; }
  .signature__social { display: flex; align-items: center; gap: 3px; }
</style>
</head>
<body>
  <section class="card-stage">
    <div class="card card--front">
      <svg class="front-badge" width="152" height="152" viewBox="0 0 152 152" aria-hidden="true">
        <circle cx="76" cy="76" r="75" fill="none" stroke="var(--badge-ring)" stroke-width="1.2"/>
      </svg>
      <div class="front-badge__name">Riverlume<br>Honey</div>
      <div class="front-ornament" role="img" aria-label="Gold foil ornamental bee pattern"></div>
    </div>

    <div class="card card--back">
      <svg class="back-mark" width="24" height="24" viewBox="0 0 24 24" aria-hidden="true">
        <circle cx="12" cy="12" r="11" fill="none" stroke="var(--foil-gold)" stroke-width="1.2"/>
      </svg>
      <div class="back-brand">Riverlume Honey</div>
      <div class="back-name">Mattias Brovell</div>
      <div class="back-title">Creative Director</div>
      <div class="back-phone">+64 2919 58 617</div>
      <div class="back-email">mattias@riverlumehoney.example</div>
      <div class="back-web">www.riverlumehoney.example</div>
    </div>
  </section>

  <section class="email-signature">
    <svg class="signature-badge" width="162" height="162" viewBox="0 0 162 162" aria-hidden="true">
      <circle cx="81" cy="81" r="80" fill="none" stroke="var(--ink)" stroke-width="1.4"/>
    </svg>
    <div class="signature-badge__name">Riverlume<br>Honey</div>

    <div class="signature">
      <div class="signature__name">Mattias Brovell</div>
      <div class="signature__title">Creative Director</div>
      <div class="signature__contacts">
        <div>+64 2919 58 617</div>
        <div>mattias@riverlumehoney.example</div>
        <div class="signature__social">
          <svg width="20" height="20" viewBox="0 0 20 20" aria-hidden="true"><circle cx="10" cy="10" r="9" fill="none" stroke="var(--ink)" stroke-width="1.5"/></svg>
          <span>/riverlumehoney</span>
        </div>
        <div class="signature__social">
          <svg width="20" height="20" viewBox="0 0 20 20" aria-hidden="true"><rect x="1" y="1" width="18" height="18" rx="4" fill="none" stroke="var(--ink)" stroke-width="1.5"/></svg>
          <span>/riverlumehoney</span>
        </div>
      </div>
    </div>
  </section>
</body>
</html>
```